Business card design for Automotive workshop

We need a business card for a new automotive repair and tyre shop called Ridgeback Prime Automotive located in New Zealand. We are a clean, modern and fresh workshop and company.

Front needs to feature logo,
my name:
Lachie Westergaard (director)

Address:
48 Marlow Lane
Whitianga 3510

Phone: 07 842 1937
Mobile: 027 519 2764
Email: office@ridgebackmotors.co.nz
Website: ridgebackmotors.co.nz

Back needs to feature an area to write down appointment details, date and time.

Also feature a list of jobs and work we do such as,
Vehicle Servicing
All Mechanical Repairs
Warrant of Fitness
Tyres & Wheel Alignments
Automotive Diagnostics
Automotive Parts & Supplies

```html
<!DOCTYPE html>
<html lang="en">
<head>
<meta charset="utf-8">
<title>Ridgeback Prime Automotive – Business Card</title>
<link href="https://fonts.googleapis.com/css2?family=Exo+2:wght@700&family=Ubuntu:wght@400&family=Arimo:wght@400;700&display=swap" rel="stylesheet">
<style>
  :root {
    --stage: #5c5c5c;
    --card-dark: #060708;
    --card-light: #dcdcdc;
    --brand-red: #e3161e;
    --ink-light: #ffffff;
    --ink-dark: #1c1c1c;
    --rule: #8a8a8a;
  }
  * { margin: 0; padding: 0; box-sizing: border-box; }
  html, body { width: 1200px; height: 900px; overflow: hidden; }
  body { background: var(--stage); position: relative; }

  .card {
    position: absolute;
    top: 200px;
    width: 310px;
    height: 502px;
    box-shadow: 2px 3px 6px rgba(0,0,0,0.45);
  }
  .card--front {
    left: 253px;
    background: var(--card-dark);
    border-radius: 62px 0 62px 0;
    font-family: "Ubuntu", sans-serif;
    color: var(--ink-light);
  }
  .card--back {
    left: 627px;
    width: 309px;
    background: var(--card-light);
    border-radius: 0 62px 0 62px;
    font-family: "Arimo", sans-serif;
    color: var(--ink-dark);
  }

  /* Front */
  .brand-name {
    position: absolute;
    left: 0; right: 0; top: 112px;
    text-align: center;
    font-family: "Exo 2", sans-serif;
    font-weight: 700;
    color: var(--brand-red);
    font-size: 24px;
    line-height: 24px;
    letter-spacing: 0.5px;
    text-transform: uppercase;
  }
  .brand-name span { display: block; font-size: 13px; line-height: 18px; letter-spacing: 2px; }

  .person { position: absolute; left: 31px; top: 272px; }
  .person__name {
    font-family: "Exo 2", sans-serif;
    font-weight: 700;
    font-size: 19px;
    color: var(--brand-red);
    letter-spacing: 0.3px;
    text-transform: uppercase;
  }
  .person__role { font-size: 14px; margin-top: 1px; }

  .address { position: absolute; left: 32px; top: 329px; font-size: 14px; line-height: 18px; font-style: normal; }

  .contacts { position: absolute; left: 34px; top: 389px; list-style: none; font-size: 14px; line-height: 18px; }
  .contacts li { display: flex; align-items: center; gap: 5px; }
  .contacts svg { width: 11px; height: 11px; fill: var(--brand-red); flex: none; }

  /* Back */
  .section-title {
    position: absolute;
    left: 60px;
    font-weight: 700;
    font-size: 18.5px;
    color: var(--brand-red);
  }
  .section-title--appointment { top: 116px; }
  .section-title--services { top: 290px; }

  .field { position: absolute; left: 61px; display: flex; align-items: flex-end; font-size: 16.5px; }
  .field--date { top: 170px; }
  .field--time { top: 215px; }
  .field__label { width: 57px; }
  .field__line { width: 133px; border-bottom: 1px solid var(--rule); margin-bottom: 4px; }

  .services { position: absolute; left: 58px; top: 332px; list-style: none; font-size: 15px; line-height: 22.8px; }
  .services li { position: relative; padding-left: 13px; }
  .services li::before {
    content: "";
    position: absolute; left: 0; top: 7px;
    width: 8px; height: 8px; border-radius: 50%;
    background: var(--brand-red);
  }
</style>
</head>
<body>

<section class="card card--front" aria-label="Business card front">
  <div class="brand-name">Ridgeback Prime<span>Automotive</span></div>

  <div class="person">
    <div class="person__name">Lachie Westergaard</div>
    <div class="person__role">Director</div>
  </div>

  <address class="address">48 Marlow Lane<br>Whitianga 3510</address>

  <ul class="contacts">
    <li>
      <svg viewBox="0 0 12 12" aria-hidden="true"><path d="M1 4.5C1 3 2.5 2 6 2s5 1 5 2.5V6H8.5V4.8h-5V6H1z M3 6.5h6l1.5 3.5h-9z"/></svg>
      07 842 1937
    </li>
    <li>
      <svg viewBox="0 0 12 12" aria-hidden="true"><path d="M3.5 0h5a1 1 0 0 1 1 1v10a1 1 0 0 1-1 1h-5a1 1 0 0 1-1-1V1a1 1 0 0 1 1-1zm0.5 1.5v7.5h4V1.5zM6 9.7a0.7 0.7 0 1 0 0.01 0z"/></svg>
      027 519 2764
    </li>
    <li>
      <svg viewBox="0 0 12 12" aria-hidden="true"><path d="M0.5 2.5h11v7h-11z" fill="none"/><path d="M0.5 2.5h11L6 6.5z M0.5 3.5v6h11v-6L6 7.6z"/></svg>
      office@ridgebackmotors.co.nz
    </li>
    <li>
      <svg viewBox="0 0 12 12" aria-hidden="true"><circle cx="6" cy="6" r="5.5"/><path d="M3 3.5l2 1-0.5 2 1.5 1v2L4 8 2.5 5z M7.5 2.5l1.5 1-1 1.5z" fill="#060708"/></svg>
      ridgebackmotors.co.nz
    </li>
  </ul>
</section>

<section class="card card--back" aria-label="Business card back">
  <h2 class="section-title section-title--appointment">NEXT APPOINTMENT</h2>

  <div class="field field--date"><span class="field__label">DATE</span><span class="field__line"></span></div>
  <div class="field field--time"><span class="field__label">TIME</span><span class="field__line"></span></div>

  <h2 class="section-title section-title--services">WORK WE DO</h2>
  <ul class="services">
    <li>Vehicle Servicing</li>
    <li>All Mechanical Repairs</li>
    <li>Warrant of Fitness</li>
    <li>Tyres &amp; Wheel Alignments</li>
    <li>Automotive Diagnostics</li>
    <li>Automotive Parts &amp; Supplies</li>
  </ul>
</section>

</body>
</html>
```